Dental specialist needs a sharp looking letterhead

I am looking for a letterhead to be used to send letters and communication between myself (a dental specialist) and other dentists.
My office is a state of the art dental specialty office.
I need to letterhead to also state:
Derek L. Halvorsen DDS
2847 Birchmont Avenue, Suite K
West Larkdale, NY 14390
(716)555-0193
fax: (716)555-0157
halvorsenpulp.com (**this email address may change)

i included my logo designs.
thank you

Target Market(s)

dentists

Industry/Entity Type

Communication

Requirements
Must have
• the included logo, whether the vertical or horizontal versions

```html
<!DOCTYPE html>
<html lang="en">
<head>
<meta charset="utf-8">
<title>Keystone Endodontics P.C. Letterhead</title>
<link rel="stylesheet" href="https://fonts.googleapis.com/css2?family=Lora:wght@400;600&display=swap">
<style>
  :root {
    --backdrop: #e9ebec;
    --paper: #ffffff;
    --brand-blue: #3a8fd1;
    --brand-green: #78b72a;
    --ink-black: #111111;
    --ink-dark: #222222;
  }
  * { box-sizing: border-box; margin: 0; padding: 0; }
  html, body {
    width: 1200px;
    height: 942px;
    overflow: hidden;
    background: var(--backdrop);
  }
  .letterhead {
    position: absolute;
    left: 260px;
    top: 31px;
    width: 680px;
    height: 880px;
    background: var(--paper);
    box-shadow: 0 2px 10px rgba(0,0,0,0.12);
    font-family: "Lora", Georgia, serif;
  }
  .divider {
    position: absolute;
    top: 0;
    bottom: 0;
    left: 196px;
    width: 5px;
    border-left: 2px solid var(--brand-green);
    border-right: 2px solid var(--brand-blue);
  }
  .brand {
    position: absolute;
    left: 22px;
    top: 48px;
    width: 160px;
    display: flex;
    align-items: center;
    gap: 8px;
  }
  .brand-dot {
    flex: none;
    width: 26px;
    height: 26px;
    border-radius: 50%;
    background: var(--brand-blue);
  }
  .brand-name {
    font-weight: 600;
    font-size: 15px;
    line-height: 1.15;
    letter-spacing: 0.06em;
    color: var(--ink-dark);
    text-transform: uppercase;
  }
  .doctor-band {
    position: absolute;
    left: 0;
    top: 118px;
    width: 196px;
    height: 30px;
    background: var(--ink-black);
    display: flex;
    align-items: center;
    justify-content: center;
  }
  .doctor-name {
    font-size: 13px;
    color: var(--brand-blue);
    letter-spacing: 0.01em;
  }
  .contact {
    position: absolute;
    left: 16px;
    bottom: 42px;
    width: 178px;
    list-style: none;
    color: var(--brand-green);
    font-size: 10.5px;
    line-height: 1.3;
  }
  .contact li {
    display: flex;
    align-items: flex-start;
    gap: 6px;
    margin-top: 5px;
  }
  .contact-icon {
    flex: none;
    width: 11px;
    height: 11px;
    margin-top: 1px;
  }
</style>
</head>
<body>
  <main class="letterhead">
    <div class="brand">
      <span class="brand-dot"></span>
      <span class="brand-name">Keystone Endodontics P.C.</span>
    </div>

    <div class="doctor-band">
      <span class="doctor-name">Derek L. Halvorsen DDS</span>
    </div>

    <div class="divider"></div>

    <ul class="contact">
      <li>
        <svg class="contact-icon" viewBox="0 0 12 12" aria-hidden="true">
          <circle cx="6" cy="6" r="6" fill="#3a8fd1"/>
          <path d="M4 3.2c.4-.3.8-.2 1 .2l.5 1c.1.3 0 .6-.2.8l-.3.3c.3.7.8 1.2 1.5 1.5l.3-.3c.2-.2.5-.3.8-.2l1 .5c.4.2.5.6.2 1l-.4.5c-.3.3-.8.4-1.2.2C5.6 8 4 6.4 3.3 4.8c-.2-.4-.1-.9.2-1.2z" fill="#fff"/>
        </svg>
        <span>(716)555-0193</span>
      </li>
      <li>
        <svg class="contact-icon" viewBox="0 0 12 12" aria-hidden="true">
          <circle cx="6" cy="6" r="6" fill="#3a8fd1"/>
          <rect x="3.5" y="2.8" width="5" height="2.2" fill="#fff"/>
          <rect x="2.6" y="5.2" width="6.8" height="2.6" rx="0.5" fill="#fff"/>
          <rect x="3.8" y="7.2" width="4.4" height="2" fill="#fff"/>
        </svg>
        <span>(716)555-0157</span>
      </li>
      <li>
        <svg class="contact-icon" viewBox="0 0 12 12" aria-hidden="true">
          <circle cx="6" cy="6" r="6" fill="#3a8fd1"/>
          <path d="M6 2.4a2.3 2.3 0 0 0-2.3 2.3C3.7 6.5 6 9.4 6 9.4s2.3-2.9 2.3-4.7A2.3 2.3 0 0 0 6 2.4z" fill="#fff"/>
          <circle cx="6" cy="4.7" r="0.9" fill="#3a8fd1"/>
        </svg>
        <span>2847 Birchmont Avenue, Suite K<br>West Larkdale, NY 14390</span>
      </li>
      <li>
        <svg class="contact-icon" viewBox="0 0 12 12" aria-hidden="true">
          <circle cx="6" cy="6" r="6" fill="#3a8fd1"/>
          <rect x="2.7" y="3.6" width="6.6" height="4.8" rx="0.5" fill="#fff"/>
          <path d="M2.9 3.9 6 6.3l3.1-2.4" stroke="#3a8fd1" stroke-width="0.7" fill="none"/>
        </svg>
        <span>derek@halvorsenpulp.com</span>
      </li>
      <li>
        <svg class="contact-icon" viewBox="0 0 12 12" aria-hidden="true">
          <circle cx="6" cy="6" r="6" fill="#3a8fd1"/>
          <circle cx="6" cy="6" r="3.4" stroke="#fff" stroke-width="0.7" fill="none"/>
          <ellipse cx="6" cy="6" rx="1.4" ry="3.4" stroke="#fff" stroke-width="0.7" fill="none"/>
          <path d="M2.6 6h6.8" stroke="#fff" stroke-width="0.7"/>
        </svg>
        <span>www.halvorsenpulp.com</span>
      </li>
    </ul>
  </main>
</body>
</html>
```